Velvet Pier Gig, Guaranteed Project

Night Club Flyer. (Need all the text, this was mis-characterized as a logo but it's a flyer. Any ideas are fine, the flyer we submitted is just a draft with the info but we want a new flyer design. Can be anything as long as it has all the text. For examples of what I like visit www.loomfield-beats.com

Target Market(s)

21 and over house/electronic music audience

Industry/Entity Type

Night Club

Logo Text

Text is on the sample

Logo styles of interest
Abstract Logo
Font styles to use
Sans Serif

Colors

Designer to choose colors to be used in the design.

Requirements
Must have
• All the text from the flyer included.
Nice to have
• Female model, classy not sexy (not mandatory). Focus should be on the band, dj's and velvet pier

```html
<!DOCTYPE html>
<html lang="en">
<head>
<meta charset="utf-8">
<title>Nocturne – Velvet Pier Hotel, Club 318</title>
<link rel="stylesheet" href="https://fonts.googleapis.com/css2?family=Audiowide&family=Kaushan+Script&display=swap">
<style>
  :root {
    --night: #0d0c17;
    --plum: #2a1836;
    --indigo: #1b2346;
    --silver: #e6e6ea;
    --steel: #9a9aa2;
    --title: #d9d9de;
    --panel: rgba(205, 205, 215, 0.42);
    --panel-edge: rgba(235, 235, 245, 0.55);
    --brush: #7c4358;
    --info: #d8b4cf;
    --script-fill: #f3d7b8;
    --script-shade: #2b1410;
  }
  * { margin: 0; padding: 0; box-sizing: border-box; }
  html, body { width: 888px; height: 1200px; overflow: hidden; background: var(--night); }
  .flyer {
    position: relative; width: 888px; height: 1200px; overflow: hidden;
    font-family: "Audiowide", sans-serif; color: var(--silver);
    background:
      radial-gradient(ellipse at 50% 12%, rgba(90, 90, 110, 0.55), transparent 55%),
      radial-gradient(ellipse at 20% 55%, rgba(70, 40, 110, 0.6), transparent 55%),
      radial-gradient(ellipse at 80% 80%, rgba(120, 40, 70, 0.45), transparent 50%),
      linear-gradient(180deg, #25232d 0%, var(--indigo) 35%, var(--plum) 65%, var(--night) 100%);
  }
  .stadium-backdrop { position: absolute; left: 0; top: 0; width: 888px; height: 360px;
    background: linear-gradient(180deg, rgba(60,60,70,.7), rgba(40,40,55,.2)); }
  .deck-backdrop { position: absolute; left: 0; top: 800px; width: 888px; height: 400px;
    background: linear-gradient(180deg, rgba(40,30,50,0), rgba(25,22,32,.9) 45%, #141219); }

  .event-title {
    position: absolute; left: 0; width: 888px; top: 72px; text-align: center;
    font-family: "Audiowide", sans-serif; font-weight: 400; font-size: 92px; line-height: 1;
    letter-spacing: 2px; color: var(--title);
  }
  .event-date { position: absolute; left: 0; width: 888px; top: 214px; text-align: center;
    font-size: 42px; color: var(--steel); letter-spacing: 1px; }
  .event-date .dash { letter-spacing: 4px; margin: 0 14px; }

  .venue-box { position: absolute; left: 36px; top: 275px; width: 824px; height: 71px;
    border: 3px solid var(--steel); display: flex; align-items: center; justify-content: center;
    font-size: 24px; color: var(--silver); background: rgba(20,20,30,.35); }

  .photo { position: absolute; }
  .photo--dj-one { left: 133px; top: 355px; width: 222px; height: 195px;
    background: linear-gradient(160deg, #6b5a55, #2e2a3a); border-radius: 6px; }
  .photo--dj-two { left: 80px; top: 555px; width: 151px; height: 145px;
    background: linear-gradient(160deg, #8a7a6a, #3a2e2c); border-radius: 6px; }
  .photo--band { left: 392px; top: 657px; width: 408px; height: 172px;
    background: linear-gradient(180deg, #3f8a3a, #1c3a22 70%, #141a18); }

  .artist-panel { position: absolute; left: 355px; width: 533px; background: var(--panel);
    border-top: 2px solid var(--panel-edge); border-left: 2px solid var(--panel-edge); text-align: center; }
  .artist-panel--one { top: 389px; height: 119px; }
  .artist-panel--two { top: 537px; height: 120px; }
  .artist-name { display: block; color: #f4f4f6; line-height: 1; white-space: nowrap; }
  .artist-city { display: block; color: #e2e2e8; letter-spacing: 7px; font-size: 24px; }
  .artist-panel--one .artist-name { font-size: 52px; letter-spacing: 14px; margin-top: 20px; }
  .artist-panel--one .artist-city { margin-top: 12px; }
  .artist-panel--two .artist-name { font-size: 50px; margin-top: 26px; }
  .artist-panel--two .artist-city { margin-top: 8px; font-size: 20px; }

  .band-block { position: absolute; left: 360px; top: 834px; width: 528px; text-align: center; }
  .band-block .artist-name { font-size: 54px; }
  .band-block .artist-city { font-size: 22px; margin-top: 6px; }

  .after-game { position: absolute; left: 14px; top: 718px; width: 390px; transform: rotate(-12deg);
    font-family: "Kaushan Script", cursive; font-size: 44px; line-height: 1.02; text-align: center;
    color: var(--script-fill); text-shadow: 3px 3px 0 var(--script-shade), 5px 5px 6px rgba(0,0,0,.6); }

  .info-band { position: absolute; left: 318px; top: 942px; width: 570px; height: 88px;
    background: var(--brush); border-radius: 30px 4px 26px 40px / 40px 6px 30px 20px; opacity: .92; }
  .info-text { position: absolute; left: 364px; top: 944px; font-size: 29px; color: var(--info); line-height: 38px; }
  .info-text .label { display: inline-block; width: 138px; }
  .info-text .indent { padding-left: 132px; }

  .footer { position: absolute; left: 0; width: 888px; top: 1112px; text-align: center;
    color: #cfcfd4; font-size: 24px; letter-spacing: 5px; line-height: 30px; }
</style>
</head>
<body>
<main class="flyer">
  <div class="stadium-backdrop" role="img" aria-label="Photo of a baseball stadium crowd at night"></div>
  <div class="deck-backdrop" role="img" aria-label="Photo of DJ turntable decks"></div>

  <h1 class="event-title">NOCTURNE</h1>
  <p class="event-date"><span class="dash">---</span>JULY 14TH 2017<span class="dash">---</span></p>

  <p class="venue-box">LIVE AT THE VELVET PIER HOTEL - CLUB 318</p>

  <div class="photo photo--dj-one" role="img" aria-label="Photo of a DJ wearing headphones"></div>
  <div class="photo photo--dj-two" role="img" aria-label="Photo of a DJ in a cap and sunglasses"></div>

  <section class="artist-panel artist-panel--one">
    <span class="artist-name">HALCYON</span>
    <span class="artist-city">SAN FRANSISCO</span>
  </section>
  <section class="artist-panel artist-panel--two">
    <span class="artist-name">MR CALLOWAY</span>
    <span class="artist-city">BAY AREA</span>
  </section>

  <div class="photo photo--band" role="img" aria-label="Photo of the three band members"></div>
  <section class="band-block">
    <span class="artist-name">LINEA NORTE</span>
    <span class="artist-city">SAN DIEGO</span>
  </section>

  <p class="after-game">Come Party After<br>The Harbor Hawks<br>beat<br>The Bay Rams</p>

  <div class="info-band"></div>
  <p class="info-text"><span class="label">INFO :</span>318SD.com<br><span class="indent">LINEANORTE.COM</span></p>

  <footer class="footer">
    318 HARBOR AVE&nbsp;&nbsp;SAN DIEGO&nbsp;&nbsp;CA 92101<br>
    T: 619 555 0130&nbsp;&nbsp;&nbsp;R : 866 555 0174
  </footer>
</main>
</body>
</html>
```